Basic Website for Vending Machine Business

We need a website designed for our vending machine business, Munchtronix, which is located in Ottawa, Canada. We requires a few links to standard sub-pages (About Us, Machines, Request a Machine, Report a Problem, Contact Us, etc.). We want it to be fun and simple. Possibly involve a vending machine in some way - make selections inside the machine the links to sub pages? Just an idea, we are very flexible though...please be creative. Attached are the drafts of our logo, we will provide the official copies of logo in near future. Key for our website is we want it visually appealing and fun, as opposed to formal.
Some slogans you may wish to use:
- Vend. Snack. Smile.
- Shop. Snack. Smile.
Target Market(s)
Small and medium size business owners.
Industry/Entity Type
Business

```html
<!DOCTYPE html>
<html lang="en">
<head>
<meta charset="utf-8">
<title>Munchtronix – Vend. Snack. Smile.</title>
<link rel="stylesheet" href="https://fonts.googleapis.com/css2?family=Open+Sans:wght@400;600;700&family=Merriweather:wght@700&display=swap">
<style>
:root{
  --orange:#f26a2b;
  --orange-dark:#d9561c;
  --ink:#3b3b3b;
  --text:#555;
  --grey-bg:#efefef;
  --card:#f1f1f1;
  --footer:#474747;
  --footer-line:#5c5c5c;
  --topbar:#444;
  --white:#fff;
}
*{margin:0;padding:0;box-sizing:border-box}
html,body{width:884px;height:1200px;overflow:hidden}
body{position:relative;background:var(--white);font-family:"Open Sans",Arial,sans-serif;color:var(--text)}
.abs{position:absolute}

/* header */
.top-strip{left:0;top:0;width:884px;height:8px;background:var(--topbar)}
.site-header{left:0;top:8px;width:884px;height:83px;background:var(--white)}
.brand{left:120px;top:28px;display:flex;align-items:center;gap:8px}
.brand-mark{width:26px;height:26px;background:var(--orange)}
.brand-name{font-size:29px;font-weight:700;color:var(--orange);letter-spacing:-0.5px;line-height:1}
.nav-home{left:460px;top:0}
.nav-link{top:34px;font-size:11px;color:var(--ink);letter-spacing:.2px}
.nav-home-label{left:460px;top:34px;width:56px;text-align:center;font-size:11px;color:var(--white)}

/* hero */
.hero{left:0;top:91px;width:884px;height:340px;background:linear-gradient(90deg,#1a1715 0%,#2c2825 35%,#4a4440 55%,#2a2624 75%,#1e1c1b 100%)}
.hero-accent{left:640px;top:91px;width:200px;height:340px;background:linear-gradient(180deg,#e8690f 0%,#f07418 60%,#c85a10 100%);opacity:.85}
.hero-title{left:122px;top:205px;font-family:"Merriweather",Georgia,serif;font-weight:700;font-size:42px;color:var(--white);letter-spacing:.5px;line-height:1}
.hero-copy{left:124px;top:255px;font-family:Arial,Helvetica,sans-serif;font-size:11.5px;line-height:15px;color:var(--white)}
.btn{background:var(--orange);color:var(--white);text-align:center;font-weight:600}
.hero-btn{left:120px;top:292px;width:169px;height:29px;line-height:29px;font-size:13px}
.hero-arrow{top:240px}

/* welcome */
.welcome{left:0;top:431px;width:884px;height:236px;background:var(--grey-bg)}
.welcome-photo{left:120px;top:472px;width:166px;height:166px;border-radius:50%;background:radial-gradient(circle at 45% 45%,#c9a66a 0%,#7a6a4e 40%,#3f9ec0 75%,#2e7ea0 100%)}
.welcome-title{left:402px;top:449px;font-size:19px;font-weight:600;color:var(--ink)}
.welcome-copy{left:403px;top:476px;width:360px;font-family:Arial,Helvetica,sans-serif;font-size:9.6px;line-height:15px;color:var(--text)}
.feature{left:401px;font-size:9.5px;font-weight:600;color:var(--ink);display:flex;align-items:center;gap:8px}
.welcome-btn{left:403px;top:588px;width:169px;height:28px;line-height:28px;font-size:13px}

/* vision */
.vision-title{left:0;top:687px;width:884px;text-align:center;font-size:16px;color:var(--ink);letter-spacing:.3px}
.vision-copy{left:0;top:712px;width:884px;text-align:center;font-family:Arial,Helvetica,sans-serif;font-size:10px;line-height:15px;color:var(--text)}
.card{top:815px;width:187px;height:203px;background:var(--card)}
.card-photo{width:98px;height:98px;border-radius:50%;border:2px solid var(--white)}
.card-title{top:876px;width:187px;text-align:center;font-size:11.5px;font-weight:600;color:var(--ink)}
.card-copy{top:900px;width:187px;text-align:center;font-family:Arial,Helvetica,sans-serif;font-size:9.8px;line-height:14px;color:var(--text)}
.card-btn{top:973px;width:72px;height:18px;line-height:18px;font-size:8px;font-weight:700}

/* footer */
.site-footer{left:0;top:1049px;width:884px;height:138px;background:var(--footer)}
.footer-band{left:0;top:1187px;width:884px;height:13px;background:var(--orange)}
.footer-heading{top:1071px;font-size:11.5px;font-weight:700;color:var(--white)}
.footer-links{top:1093px;list-style:none;font-family:Arial,Helvetica,sans-serif;font-size:8.5px;line-height:13.3px;color:var(--white)}
.footer-divider{top:1070px;width:1px;height:85px;background:var(--footer-line)}
.footer-brand{left:406px;top:1085px;display:flex;align-items:center;gap:6px}
.footer-brand .brand-mark{width:20px;height:20px}
.footer-brand .brand-name{font-size:22px}
.email-field{left:404px;top:1128px;width:125px;height:19px;background:#6a6a6a;color:#cfcfcf;font-size:8px;line-height:19px;padding-left:8px}
.subscribe-btn{left:529px;top:1128px;width:64px;height:19px;line-height:19px;font-size:7.5px;font-weight:700}
.social{left:633px;top:1094px}
.copyright{left:635px;top:1124px;font-family:Arial,Helvetica,sans-serif;font-size:8px;color:var(--white)}
</style>
</head>
<body>

<div class="abs top-strip"></div>
<header class="abs site-header"></header>
<div class="abs brand"><span class="brand-mark"></span><span class="brand-name">Munchtronix</span></div>

<svg class="abs nav-home" width="56" height="67" viewBox="0 0 56 67" aria-hidden="true">
  <path d="M0 8 H56 V56 L28 67 L0 56 Z" fill="#f26a2b"/>
  <rect x="23" y="16" width="10" height="10" fill="none" stroke="#fff" stroke-width="1.6"/>
</svg>
<div class="abs nav-home-label">HOME</div>
<nav>
  <div class="abs nav-link" style="left:540px">ABOUT US</div>
  <div class="abs nav-link" style="left:619px">MACHINES</div>
  <div class="abs nav-link" style="left:700px">CONTACT US</div>
</nav>

<section>
  <div class="abs hero" role="img" aria-label="Blurred photo of a person in an orange sweater stirring a cup of vending machine coffee"></div>
  <div class="abs hero-accent" aria-hidden="true"></div>
  <h1 class="abs hero-title">Vend. Snack. Smile.</h1>
  <p class="abs hero-copy">We are the largest provider of portable affordable and portable vending machine<br>orem Ipsum is simply dummy text of the printing and typesetting</p>
  <div class="abs btn hero-btn">Request a Machine</div>
  <svg class="abs hero-arrow" style="left:66px" width="24" height="56" viewBox="0 0 24 56" aria-hidden="true"><path d="M22 2 L3 28 L22 54" fill="none" stroke="#bbb" stroke-width="1.2"/></svg>
  <svg class="abs hero-arrow" style="left:806px" width="24" height="56" viewBox="0 0 24 56" aria-hidden="true"><path d="M2 2 L21 28 L2 54" fill="none" stroke="#bbb" stroke-width="1.2"/></svg>
</section>

<section>
  <div class="abs welcome"></div>
  <svg class="abs" style="left:0;top:660px" width="884" height="10" viewBox="0 0 884 10" aria-hidden="true">
    <path d="M0 0 H884 V2 L878 8 L872 2 L866 8 L860 2 L854 8 L848 2 L842 8 L836 2 L830 8 L824 2 L818 8 L812 2 L806 8 L800 2 L794 8 L788 2 L782 8 L776 2 L770 8 L764 2 L758 8 L752 2 L746 8 L740 2 L734 8 L728 2 L722 8 L716 2 L710 8 L704 2 L698 8 L692 2 L686 8 L680 2 L674 8 L668 2 L662 8 L656 2 L650 8 L644 2 L638 8 L632 2 L626 8 L620 2 L614 8 L608 2 L602 8 L596 2 L590 8 L584 2 L578 8 L572 2 L566 8 L560 2 L554 8 L548 2 L542 8 L536 2 L530 8 L524 2 L518 8 L512 2 L506 8 L500 2 L494 8 L488 2 L482 8 L476 2 L470 8 L464 2 L458 8 L452 2 L446 8 L440 2 L434 8 L428 2 L422 8 L416 2 L410 8 L404 2 L398 8 L392 2 L386 8 L380 2 L374 8 L368 2 L362 8 L356 2 L350 8 L344 2 L338 8 L332 2 L326 8 L320 2 L314 8 L308 2 L302 8 L296 2 L290 8 L284 2 L278 8 L272 2 L266 8 L260 2 L254 8 L248 2 L242 8 L236 2 L230 8 L224 2 L218 8 L212 2 L206 8 L200 2 L194 8 L188 2 L182 8 L176 2 L170 8 L164 2 L158 8 L152 2 L146 8 L140 2 L134 8 L128 2 L122 8 L116 2 L110 8 L104 2 L98 8 L92 2 L86 8 L80 2 L74 8 L68 2 L62 8 L56 2 L50 8 L44 2 L38 8 L32 2 L26 8 L20 2 L14 8 L8 2 L2 8 L0 6 Z" fill="#efefef"/>
  </svg>
  <div class="abs welcome-photo" role="img" aria-label="Round photo of two smiling women at a vending machine"></div>
  <svg class="abs" style="left:292px;top:454px" width="84" height="56" viewBox="0 0 84 56" aria-hidden="true">
    <path d="M4 52 C20 24 44 8 76 8" fill="none" stroke="#a8341a" stroke-width="2"/>
    <path d="M70 2 L80 8 L70 14" fill="none" stroke="#a8341a" stroke-width="2"/>
  </svg>
  <h2 class="abs welcome-title">Welcome to Munchtronix</h2>
  <p class="abs welcome-copy">Lorem Ipsum is simply dummy text of the printing and typesetting industry. Lorem Ipsum has been the industry's standard dummy text ever since the 1500sLorem Ipsum is the simply dummy text of the printing and typesetting industry.</p>
  <div class="abs feature" style="top:531px"><svg width="10" height="9" viewBox="0 0 10 9" aria-hidden="true"><path d="M1 5 L4 8 L9 1" fill="none" stroke="#f26a2b" stroke-width="2"/></svg>Modern and Affordable Price</div>
  <div class="abs feature" style="top:553px"><svg width="10" height="9" viewBox="0 0 10 9" aria-hidden="true"><path d="M1 5 L4 8 L9 1" fill="none" stroke="#f26a2b" stroke-width="2"/></svg>Largest Portable&nbsp; Vending Machin Provider</div>
  <div class="abs btn welcome-btn">Report a Problem</div>
</section>

<section>
  <h2 class="abs vision-title">VISION OF OUR COMPANY</h2>
  <p class="abs vision-copy">Lorem Ipsum is simply dummy text of the printing and typesetting industry. Lorem Ipsum has been<br>the industry's standard dummy text ever since Lorem Ipsum is simply dummy text of the</p>

  <div class="abs card" style="left:120px"></div>
  <div class="abs card-photo" style="left:164px;top:765px;background:linear-gradient(135deg,#dfe4ea 0%,#9aa4b0 55%,#c2457a 100%)" role="img" aria-label="Round photo of a hand choosing a snack at a vending machine"></div>
  <h3 class="abs card-title" style="left:120px">TREAT YOUR CUSTOMERS</h3>
  <p class="abs card-copy" style="left:120px">Lorem Ipsum is simply dummy text<br>of the printing and typesetting Lorem<br>Ipsum has been</p>
  <div class="abs btn card-btn" style="left:168px">KNOW MORE</div>

  <div class="abs card" style="left:344px"></div>
  <div class="abs card-photo" style="left:388px;top:765px;background:radial-gradient(circle at 50% 60%,#c8842e 0%,#5a3f2a 40%,#2a2523 100%)" role="img" aria-label="Round photo of coffee pouring from a machine spout"></div>
  <h3 class="abs card-title" style="left:344px">SIMPLE AND USER-FRIENDLY</h3>
  <p class="abs card-copy" style="left:344px">Lorem Ipsum is simply dummy text<br>of the printing and typesetting Lorem<br>Ipsum has been</p>
  <div class="abs btn card-btn" style="left:392px">KNOW MORE</div>

  <div class="abs card" style="left:568px"></div>
  <div class="abs card-photo" style="left:612px;top:765px;background:radial-gradient(circle at 55% 60%,#e9d8c4 0%,#a86a3c 45%,#5a3520 100%)" role="img" aria-label="Round photo of cups of coffee seen from above"></div>
  <h3 class="abs card-title" style="left:568px">AFFORDABLE SERVICES</h3>
  <p class="abs card-copy" style="left:568px">Lorem Ipsum is simply dummy text<br>of the printing and typesetting Lorem<br>Ipsum has been</p>
  <div class="abs btn card-btn" style="left:616px">KNOW MORE</div>
</section>

<footer>
  <div class="abs site-footer"></div>
  <div class="abs footer-band"></div>

  <div class="abs footer-heading" style="left:120px">WELCOME</div>
  <ul class="abs footer-links" style="left:120px">
    <li>Home</li><li>About Us</li><li>Machines</li><li>Contact Us</li><li>Help/Faq</li>
  </ul>
  <div class="abs footer-heading" style="left:271px">QUICK MENU</div>
  <ul class="abs footer-links" style="left:272px">
    <li>Report a Problem</li><li>Request a Machine</li><li>Our Location</li><li>Terms of Use</li><li>Privacy Policy</li>
  </ul>

  <div class="abs footer-divider" style="left:388px"></div>
  <div class="abs footer-brand"><span class="brand-mark"></span><span class="brand-name">Munchtronix</span></div>
  <div class="abs email-field">Your email address</div>
  <div class="abs btn subscribe-btn">SUBSCRIBE</div>
  <div class="abs footer-divider" style="left:613px"></div>

  <div class="abs footer-heading" style="left:635px;top:1073px">WE'RE SOCIAL</div>
  <svg class="abs social" width="128" height="20" viewBox="0 0 128 20" aria-label="Social links">
    <g fill="none" stroke="#f26a2b" stroke-width="1.5">
      <circle cx="10" cy="10" r="8.5"/><circle cx="35" cy="10" r="8.5"/><circle cx="60" cy="10" r="8.5"/><circle cx="86" cy="10" r="8.5"/><circle cx="112" cy="10" r="8.5"/>
    </g>
  </svg>
  <div class="abs copyright">© 2015 www.munchtronix.com</div>
</footer>

</body>
</html>
```